I need jar labels, and other types to include round and cigar band with an already designed logo

Need a round sticker to place on products, jar labels, 3 sizes with 1 label having 3 different names. also reflect my design on a thank you card and round sticker
I would like a 10 " cigar band with my logo in the middle for handmade bars of soap

Target Market(s)

This project will be for labeling my products for my e-commerce business

Industry/Entity Type

Beauty

Font styles to use
Serif

Colors
e667a6
ffcf3e

Requirements
Must have
• The labels must contain my logo. I need (4) 1.5" X 4" label with my logo and the words: Handmade Sugar Scrub, Handmade Whipped Body Butter, Handmade Whipped Soap Scrub, Handmade Salt Scrub

I also must have a round sticker 2' in diameter with my logo in Gold

I also need a round sticker I rose gold that reflects my logo and says thank you for supporting my small business.
Nice to have
• I want round and rectangle labels for products that contain my logo. I also need thank you cards and thank you for your order sticker with my logo
Should not have
• do not change the color of my logo and make the print on the labels in Black

```html
<!DOCTYPE html>
<html lang="en">
<head>
<meta charset="utf-8">
<title>Lather Lane – Sugar Scrub Labels</title>
<link rel="stylesheet" href="https://fonts.googleapis.com/css2?family=Jost:wght@400;500&family=Mr+Dafoe&display=swap">
<style>
  :root {
    --canvas: #f3f2f3;
    --label-white: #ffffff;
    --berry: #db64a5;
    --honey: #e9c53f;
    --rose-gold: #e3a49c;
    --ink: #161616;
    --paper-text: #ffffff;
  }
  * { margin: 0; padding: 0; box-sizing: border-box; }
  html, body { width: 1200px; height: 1200px; overflow: hidden; }
  body { background: var(--canvas); position: relative; font-family: "Jost", sans-serif; }

  .product-row { position: absolute; left: 0; width: 1200px; height: 300px; }
  .product-row--berry { top: 230px; }
  .product-row--honey { top: 660px; }

  .jar-label {
    position: absolute; left: 140px; top: 30px;
    width: 540px; height: 230px;
    background: var(--label-white);
    box-shadow: 0 2px 10px rgba(0,0,0,0.08);
  }
  .jar-label__band { position: absolute; inset: 0; width: 100%; height: 100%; }
  .jar-label__band path { fill: var(--band); }
  .product-row--berry { --band: var(--berry); --label-text: var(--paper-text); }
  .product-row--honey { --band: var(--honey); --label-text: var(--ink); }

  .brand-seal {
    position: absolute; left: 18px; top: 29px;
    width: 172px; height: 172px; border-radius: 50%;
    border: 2px solid var(--rose-gold);
    display: flex; align-items: center; justify-content: center;
  }
  .brand-seal__name {
    font-family: "Jost", sans-serif; font-weight: 500;
    font-size: 22px; letter-spacing: 1px; color: var(--rose-gold);
    text-transform: uppercase; text-align: center; line-height: 1.2;
  }

  .jar-label__copy {
    position: absolute; left: 245px; right: 20px; top: 48px;
    text-align: center; color: var(--label-text);
  }
  .jar-label__script {
    font-family: "Mr Dafoe", cursive; font-size: 50px; line-height: 1;
    margin-left: 10px;
  }
  .jar-label__product {
    font-family: "Jost", sans-serif; font-weight: 500;
    font-size: 38px; letter-spacing: 0.5px; margin-top: 18px;
  }

  .lid-sticker {
    position: absolute; left: 790px; top: 10px;
    width: 280px; height: 280px; border-radius: 50%;
    background: var(--label-white);
    box-shadow: 0 2px 10px rgba(0,0,0,0.08);
    display: flex; align-items: center; justify-content: center;
  }
  .lid-sticker .brand-seal {
    position: static; width: 190px; height: 190px;
  }
  .lid-sticker .brand-seal__name { font-size: 24px; }
</style>
</head>
<body>
  <section class="product-row product-row--berry">
    <div class="jar-label">
      <svg class="jar-label__band" viewBox="0 0 540 230" aria-hidden="true">
        <path d="M155,12 L540,12 L540,218 L155,218 A113 113 0 0 0 155,12 Z"/>
      </svg>
      <div class="brand-seal"><span class="brand-seal__name">Lather<br>Lane</span></div>
      <div class="jar-label__copy">
        <div class="jar-label__script">Handmade</div>
        <div class="jar-label__product">SUGAR SCRUB</div>
      </div>
    </div>
    <div class="lid-sticker">
      <div class="brand-seal"><span class="brand-seal__name">Lather<br>Lane</span></div>
    </div>
  </section>

  <section class="product-row product-row--honey">
    <div class="jar-label">
      <svg class="jar-label__band" viewBox="0 0 540 230" aria-hidden="true">
        <path d="M155,12 L540,12 L540,218 L155,218 A113 113 0 0 0 155,12 Z"/>
      </svg>
      <div class="brand-seal"><span class="brand-seal__name">Lather<br>Lane</span></div>
      <div class="jar-label__copy">
        <div class="jar-label__script">Handmade</div>
        <div class="jar-label__product">SUGAR SCRUB</div>
      </div>
    </div>
    <div class="lid-sticker">
      <div class="brand-seal"><span class="brand-seal__name">Lather<br>Lane</span></div>
    </div>
  </section>
</body>
</html>
```